Acupuncture business needs business card design

I need a business card for an acupuncture clinic called "Summit Wellpath"
It will need the following details:
My name: Marcus Thelwick
Acupuncturist
Member KPTG
BVF Treatment Provider
Ph numbers: 482 1358 027 514 3820
Email: marcus@swpath.example.nz
On the back it will need a table with 2 columns for appointments, one column for time and one for date.

Industry/Entity Type

Clinic

Contact Information for Business Card

Marcus Thelwick
Acupuncturist
Member KPTG
BVF Treatment Provider
Email: marcus@swpath.example.nz

Requirements
Must have
• Marcus Thelwick
• Acupuncturist
• Member KPTG
• BVF Treatment Provider
• Ph numbers: 482 1358 027 514 3820
• Email: marcus@swpath.example.nz
• On the back it will need a table with 2 columns for appointments, one column for time and one for date.

```html
<!DOCTYPE html>
<html lang="en">
<head>
<meta charset="utf-8">
<title>Summit Wellpath – Business Card</title>
<link href="https://fonts.googleapis.com/css2?family=Open+Sans:wght@400;600;700&display=swap" rel="stylesheet">
<style>
  :root {
    --sky: #17a4dc;
    --teal: #0f6683;
    --teal-deep: #0b5a74;
    --ink: #1c1c1c;
    --dots: #6a6a6a;
    --paper: #ffffff;
    --backdrop: #e9ebed;
  }
  * { box-sizing: border-box; margin: 0; padding: 0; }
  html, body { width: 1200px; height: 1000px; overflow: hidden; }
  body {
    background: var(--backdrop);
    font-family: "Open Sans", Arial, sans-serif;
    position: relative;
  }
  .card {
    position: absolute;
    left: 250px;
    width: 700px;
    height: 400px;
    background: var(--paper);
    box-shadow: 0 6px 20px rgba(0,0,0,.15);
    overflow: hidden;
  }
  .card--back { top: 60px; }
  .card--front { top: 540px; }

  .brand { position: absolute; display: flex; align-items: center; gap: 18px; }
  .brand__dot { width: 56px; height: 56px; border-radius: 50%; background: var(--teal); flex: none; }
  .brand__name { font-size: 50px; font-weight: 600; color: var(--sky); line-height: 1; letter-spacing: -0.5px; }
  .brand__tagline {
    font-size: 15px; letter-spacing: 6.5px; color: var(--sky);
    text-transform: uppercase; margin-top: 4px; line-height: 1;
  }
  .card--front .brand { left: 70px; top: 70px; }
  .card--back .brand { left: 120px; top: 40px; }
  .card--back .brand__dot { width: 44px; height: 44px; }
  .card--back .brand__name { font-size: 40px; }
  .card--back .brand__tagline { font-size: 12px; letter-spacing: 5.5px; }

  /* Front */
  .person { position: absolute; left: 55px; top: 195px; z-index: 1; }
  .person__name { font-size: 30px; font-weight: 600; color: var(--sky); line-height: 1.1; margin-left: 22px; }
  .person__role { font-size: 20px; color: var(--ink); line-height: 1.3; }
  .person__role:nth-of-type(1) { margin-left: 15px; }
  .person__role:nth-of-type(2) { margin-left: 8px; }

  .divider { position: absolute; left: 350px; top: 225px; width: 1px; height: 100px; background: #555; }
  .contacts { position: absolute; left: 372px; top: 225px; list-style: none; z-index: 1; }
  .contacts li { display: flex; align-items: center; gap: 12px; font-size: 19px; color: var(--ink); height: 36px; white-space: nowrap; }
  .contacts svg { width: 19px; height: 19px; fill: var(--teal); flex: none; }

  .wave { position: absolute; left: 0; bottom: 0; width: 700px; height: 200px; }

  /* Back */
  .appointment__title {
    position: absolute; left: 0; right: 0; top: 125px; text-align: center;
    font-size: 26px; font-weight: 700; color: var(--teal);
  }
  .appointment {
    position: absolute; left: 60px; top: 180px; width: 580px;
    border-collapse: collapse; table-layout: fixed;
  }
  .appointment td { height: 48px; vertical-align: bottom; padding-bottom: 6px; }
  .appointment .label { color: var(--sky); font-size: 19px; white-space: nowrap; }
  .appointment .line { border-bottom: 2px dotted var(--dots); }
  .appointment .label--time { padding-left: 20px; }
</style>
</head>
<body>

  <section class="card card--back" aria-label="Card back: appointment table">
    <div class="brand">
      <span class="brand__dot"></span>
      <div>
        <div class="brand__name">Summit Wellpath</div>
        <div class="brand__tagline">Acupuncture Physiotherapy</div>
      </div>
    </div>
    <h2 class="appointment__title">Your next Appointment</h2>
    <table class="appointment">
      <colgroup>
        <col style="width:100px"><col style="width:250px"><col style="width:80px"><col style="width:150px">
      </colgroup>
      <tr><td class="label">Day/Date</td><td class="line"></td><td class="label label--time">Time</td><td class="line"></td></tr>
      <tr><td class="label">Day/Date</td><td class="line"></td><td class="label label--time">Time</td><td class="line"></td></tr>
      <tr><td class="label">Day/Date</td><td class="line"></td><td class="label label--time">Time</td><td class="line"></td></tr>
      <tr><td class="label">Day/Date</td><td class="line"></td><td class="label label--time">Time</td><td class="line"></td></tr>
    </table>
  </section>

  <section class="card card--front" aria-label="Card front">
    <svg class="wave" viewBox="0 0 700 200" preserveAspectRatio="none" aria-hidden="true">
      <path d="M0 95 C 80 170, 260 150, 420 150 C 560 150, 640 165, 700 200 L700 200 L0 200 Z" fill="var(--sky)"/>
      <path d="M0 108 C 90 182, 270 165, 430 163 C 570 162, 650 180, 700 210 L700 200 L0 200 Z" fill="var(--teal-deep)"/>
    </svg>

    <div class="brand">
      <span class="brand__dot"></span>
      <div>
        <div class="brand__name">Summit Wellpath</div>
        <div class="brand__tagline">Acupuncture Physiotherapy</div>
      </div>
    </div>

    <div class="person">
      <div class="person__name">Marcus Thelwick</div>
      <p class="person__role">Acupuncturist</p>
      <p class="person__role">Member KPTG</p>
      <p class="person__role">BVF Treatment Provider</p>
    </div>

    <div class="divider"></div>

    <ul class="contacts">
      <li>
        <svg viewBox="0 0 24 24" aria-hidden="true"><path d="M3 9c0-3 4-5 9-5s9 2 9 5v1h-4V8.5c-1.3-.6-3-.9-5-.9s-3.7.3-5 .9V10H3V9zm4 2h10l2 8H5l2-8zm5 1.5a3 3 0 100 6 3 3 0 000-6z"/></svg>
        482 1358
      </li>
      <li>
        <svg viewBox="0 0 24 24" aria-hidden="true"><path d="M3 9c0-3 4-5 9-5s9 2 9 5v1h-4V8.5c-1.3-.6-3-.9-5-.9s-3.7.3-5 .9V10H3V9zm4 2h10l2 8H5l2-8zm5 1.5a3 3 0 100 6 3 3 0 000-6z"/></svg>
        027 514 3820
      </li>
      <li>
        <svg viewBox="0 0 24 24" aria-hidden="true"><path d="M2 5h20v14H2V5zm2 2v.5l8 5.5 8-5.5V7H4z"/></svg>
        marcus@swpath.example.nz
      </li>
    </ul>
  </section>

</body>
</html>
```